Pause Your Day And Browse- PYDB poster

I am the Vice President of Advocacy for the Coastline Shelfkeepers Guild. I am looking to have a set of posters made for PYDB (Pause Your Day and Browse) October 23. PYDB is a time when all school children in BC are encouraged to Pause Your Day and Browse for 15-20 minutes at some point in their day.

I would like to get a set of 2 digital posters designed (if possible it would be nice to have the option to print to both 11 x 17 and 8.5 x 11 paper). We need a poster that is high school (Grade 8-12) appropriate and one that is elementary (Grade k-7) appropriate. Both posters need to be replicated in French. All posters need to have the KWNU logo on them as well as the Coastline Shelfkeepers Guild Logo.

Here is a link to last year's successful design http://kwnu-example.org/csg/info/advocacy.html
There are two additional samples in the uploaded files section.

Each poster needs to have the following information:

-Pause Your Day and Browse (PYDB)
- The date Monday, October 23, 2017
-the logo for the KWNU (attached)
-the logo for the CSG (attached)- the logos do not have to be large.

Target Market(s)

Children ages 5-12 and 12-17 as well as their teachers

Industry/Entity Type

Teacher

Font styles to use
Sans Serif

Requirements
Must have
• Must have both logos- colours may be changed for either or both
Nice to have
• Clear, Bright lettering. Images of child or children enjoying reading
Should not have
• stereotypes

```html
<!DOCTYPE html>
<html lang="en">
<head>
<meta charset="utf-8">
<title>Pause Your Day And Browse – October 23, 2017</title>
<link rel="stylesheet" href="https://fonts.googleapis.com/css2?family=Archivo+Black&family=Arimo:wght@700&display=swap">
<style>
  :root {
    --page: #ffffff;
    --kraft: #b39a7c;
    --kraft-light: #bca486;
    --kraft-dark: #a88f71;
    --blue: #3a6fb3;
    --blue-deep: #1f3552;
    --orange: #f4a22f;
    --orange-deep: #5a3a12;
    --green: #8cc63f;
    --green-deep: #2f4a1a;
    --pink: #e06aa8;
    --pink-deep: #4f2340;
    --shadow: #121212;
    --white: #ffffff;
    --logo-ink: #1f3f7a;
  }
  * { box-sizing: border-box; margin: 0; padding: 0; }
  html, body { width: 928px; height: 1200px; overflow: hidden; background: var(--page); }
  .poster { position: relative; width: 928px; height: 1200px; background: var(--page); }
  .kraft-field {
    position: absolute; left: 32px; top: 41px; width: 864px; height: 1119px;
    background: linear-gradient(180deg, var(--kraft-light), var(--kraft) 50%, var(--kraft-dark));
  }
  .reader-art {
    position: absolute; left: 151px; top: 174px; width: 499px; height: 313px;
    border-radius: 40px 40px 0 0;
    background: linear-gradient(90deg, #e17bb8 0%, #f2a43c 30%, #4a78c0 60%, #8fca4a 100%);
    opacity: .85;
  }
  .headline { position: absolute; left: 180px; top: 480px; width: 640px; height: 380px; }
  .headline text { font-family: "Archivo Black", "Arial Black", sans-serif; }
  .event-date {
    position: absolute; left: 0; width: 100%; top: 870px; padding-left: 60px;
    text-align: center; color: var(--white);
    font-family: "Arimo", Arial, sans-serif; font-weight: 700; font-size: 32px;
  }
  .partner-band {
    position: absolute; left: 32px; top: 969px; width: 864px; height: 162px;
    background: var(--white);
    display: flex; align-items: center; justify-content: center; gap: 44px;
  }
  .partner {
    display: flex; align-items: center; gap: 10px;
    font-family: "Arimo", Arial, sans-serif; font-weight: 700; color: var(--logo-ink);
  }
  .partner-name { font-size: 26px; line-height: 1; }
  .partner-sub { font-size: 11px; line-height: 1.25; max-width: 110px; }
  .partner-stack { display: flex; flex-direction: column; gap: 6px; }
  .partner-dot { width: 64px; height: 64px; border-radius: 50%; background: var(--logo-ink); flex: none; }
</style>
</head>
<body>
<main class="poster">
  <div class="kraft-field"></div>

  <div class="reader-art" role="img" aria-label="Illustration of two children standing back to back, each reading an open book"></div>

  <svg class="headline" viewBox="0 0 640 380" aria-label="Pause Your Day And Browse">
    <g class="word word-pause">
      <text x="81" y="117" font-size="124" textLength="400" lengthAdjust="spacingAndGlyphs" fill="var(--shadow)">PAUSE</text>
      <text x="75" y="110" font-size="124" textLength="400" lengthAdjust="spacingAndGlyphs" fill="var(--blue-deep)">PAUSE</text>
      <text x="69" y="103" font-size="124" textLength="400" lengthAdjust="spacingAndGlyphs" fill="var(--blue)">PAUSE</text>
    </g>
    <g class="word word-your-day">
      <text x="81" y="184" font-size="84" textLength="520" lengthAdjust="spacingAndGlyphs" fill="var(--shadow)">YOUR DAY</text>
      <text x="75" y="177" font-size="84" textLength="520" lengthAdjust="spacingAndGlyphs" fill="var(--orange-deep)">YOUR DAY</text>
      <text x="69" y="170" font-size="84" textLength="520" lengthAdjust="spacingAndGlyphs" fill="var(--orange)">YOUR DAY</text>
    </g>
    <g class="word word-and">
      <text x="81" y="252" font-size="76" textLength="160" lengthAdjust="spacingAndGlyphs" fill="var(--shadow)">AND</text>
      <text x="75" y="245" font-size="76" textLength="160" lengthAdjust="spacingAndGlyphs" fill="var(--green-deep)">AND</text>
      <text x="69" y="238" font-size="76" textLength="160" lengthAdjust="spacingAndGlyphs" fill="var(--green)">AND</text>
    </g>
    <g class="word word-browse">
      <text x="251" y="272" font-size="110" textLength="346" lengthAdjust="spacingAndGlyphs" fill="var(--shadow)">BROWSE</text>
      <text x="245" y="265" font-size="110" textLength="346" lengthAdjust="spacingAndGlyphs" fill="var(--pink-deep)">BROWSE</text>
      <text x="239" y="258" font-size="110" textLength="346" lengthAdjust="spacingAndGlyphs" fill="var(--pink)">BROWSE</text>
    </g>
  </svg>

  <p class="event-date">October 23, 2017</p>

  <footer class="partner-band">
    <div class="partner partner-guild">
      <div class="partner-stack">
        <span class="partner-name">CSG</span>
        <span class="partner-sub">Coastline Shelfkeepers Guild</span>
      </div>
    </div>
    <div class="partner partner-event">
      <span class="partner-name">PYDB</span>
    </div>
    <div class="partner partner-union">
      <span class="partner-dot"></span>
      <span class="partner-name">KWNU</span>
    </div>
  </footer>
</main>
</body>
</html>
```